Zero Tax Seminar Postcard Design

I need a postcard designed that is 5.5" x 8.5". Color front and back with space for an address block and postal indicia. I will provide the bullet points and copy. I need assistance with the layout, organization and perhaps a couple of images, etc. This postcard will drive individuals to a web site to register for a 90-minute seminar teaching them how to minimize or eliminate their income taxes during retirement.
Target Market(s)
Married Couples, ages 50 - 70. Successful and affluent. People that appreciate and value professional advice and relationships.
Requirements
Must have
- Bright and Bold.  Compelling and attention grabbing.
Call to action #1 - Go to website immediately for further information.
Call to action #2 - Call the office immediately to register.

```html
<!DOCTYPE html>
<html lang="en">
<head>
<meta charset="utf-8">
<title>Zero Tax Seminar Postcard</title>
<link rel="stylesheet" href="https://fonts.googleapis.com/css2?family=Federo&family=Sorts+Mill+Goudy&family=Russo+One&family=Didact+Gothic&display=swap">
<style>
  :root {
    --green: #93c762;
    --navy: #3a4a84;
    --slate: #4d6a8c;
    --mint: #b5e08a;
    --ink: #1d2a5a;
    --paper: #ffffff;
    --shadow: 0 3px 8px rgba(0,0,0,.35);
  }
  * { box-sizing: border-box; margin: 0; padding: 0; }
  html, body { width: 1200px; height: 1000px; overflow: hidden; background: var(--paper); }
  .canvas { position: relative; width: 1200px; height: 1000px; }

  .card { position: absolute; overflow: hidden; box-shadow: var(--shadow); background: var(--paper); }

  /* Front */
  .front { left: 67px; top: 65px; width: 594px; height: 405px; }
  .front .photo { position: absolute; inset: 0;
    background: linear-gradient(90deg, #eef1f4 0%, #e6e8ea 45%, #e9dfcf 62%, #d9cbb3 100%),
                linear-gradient(180deg, #f1f3f6 0%, #dfe6ec 55%, #e7dccb 75%, #e0d4c2 100%);
    background-blend-mode: multiply; }
  .front .band-top { position: absolute; left: 0; top: 0; width: 594px; height: 35px; background: var(--green); opacity: .95; }
  .front .bar-top { position: absolute; left: 0; top: 35px; width: 547px; height: 11px; background: var(--navy); }
  .front .bar-bottom { position: absolute; left: 45px; top: 360px; width: 549px; height: 12px; background: var(--green); }
  .front .band-bottom { position: absolute; left: 0; top: 372px; width: 594px; height: 33px; background: var(--navy); }
  .front .headline { position: absolute; left: 0; top: 110px; width: 296px; text-align: center;
    font-family: "Federo", sans-serif; font-size: 31px; color: var(--navy); }
  .front .pitch { position: absolute; left: 0; top: 158px; width: 300px; text-align: center;
    font-family: "Sorts Mill Goudy", serif; font-size: 15.5px; line-height: 24.6px; color: #111; }

  /* Back */
  .back { left: 499px; top: 528px; width: 594px; height: 407px; }
  .back .panel { position: absolute; left: 0; top: 0; width: 332px; height: 407px; background: var(--green); }
  .back .snap { position: absolute; border: 4px solid #fff; box-shadow: 0 1px 3px rgba(0,0,0,.4); }
  .snap.s1 { left: 6px; top: -2px; width: 118px; height: 72px; background: linear-gradient(135deg,#c77a3a,#e7c49a 55%,#8fb35a); transform: rotate(4deg); }
  .snap.s2 { left: -2px; top: 72px; width: 92px; height: 72px; background: linear-gradient(180deg,#6ea1d6,#b8d3ea 60%,#6d8a5a); }
  .snap.s3 { left: -2px; top: 270px; width: 62px; height: 66px; background: linear-gradient(180deg,#5b93d2,#c7dff3 60%,#b9a98e); }
  .snap.s4 { left: 2px; top: 334px; width: 126px; height: 76px; background: linear-gradient(180deg,#6aa0d8,#9ec3e3 45%,#7b6b5c); transform: rotate(-3deg); }
  .back .title { position: absolute; left: 120px; top: 28px; width: 192px; text-align: center;
    font-family: "Russo One", sans-serif; font-size: 17px; line-height: 22px; color: var(--navy); }
  .back .register { position: absolute; left: 0; top: 144px; width: 332px; height: 127px; background: var(--slate);
    padding-top: 8px; text-align: center; font-family: "Didact Gothic", sans-serif; font-size: 12px; line-height: 12.6px; color: var(--mint); }
  .register p + p { margin-top: 12.6px; }
  .back .signoff { position: absolute; left: 140px; top: 297px; width: 160px; text-align: center;
    font-family: "Didact Gothic", sans-serif; font-size: 9.5px; line-height: 12px; color: var(--ink); }
  .back .signature { display: block; margin: 3px auto 4px; width: 110px; height: 22px; }
  .back .credit { font-size: 9.3px; line-height: 10.5px; }
  .back .postage { position: absolute; left: 491px; top: 24px; width: 81px; height: 81px; border: 3px solid #111;
    display: flex; align-items: center; justify-content: center; text-align: center;
    font-family: "Didact Gothic", sans-serif; font-size: 13px; line-height: 14px; color: #111; }
</style>
</head>
<body>
<div class="canvas">

  <section class="card front">
    <div class="photo" role="img" aria-label="Photo of a smiling retired couple embracing on a beach"></div>
    <div class="band-top"></div>
    <div class="bar-top"></div>
    <h1 class="headline">A Unique</h1>
    <p class="pitch">One-Of-A-Kind Program Reveals<br>Little Known Secrets<br>Used By America’s Wealthiest Families<br>To Reduce And Even Eliminate<br>Their Income Taxes<br>During Their Retirement Years</p>
    <div class="bar-bottom"></div>
    <div class="band-bottom"></div>
  </section>

  <section class="card back">
    <div class="panel">
      <div class="snap s1" role="img" aria-label="Photo of a couple enjoying autumn outdoors"></div>
      <div class="snap s2" role="img" aria-label="Photo of a couple riding a scooter"></div>
      <h2 class="title">The Zero<br>Tax Solution<br>A Free Educational<br>Seminar</h2>
      <div class="register">
        <p>Register Today!!<br>Visit www.HarlanReeveWealthGroup.Com right away<br>to learn about upcoming dates, times and locations</p>
        <p>Call our office to register immediately (555) 014-2290</p>
        <p>“I personally guarantee – when you attend this seminar,<br>your view of the complex world of Wealth<br>and Taxation will be dramatically different”</p>
      </div>
      <div class="snap s3" role="img" aria-label="Photo of a couple hugging outdoors"></div>
      <div class="snap s4" role="img" aria-label="Photo of a couple relaxing by the sea"></div>
      <div class="signoff">
        <p>Remember, Stay Focused,<br>Stay Diligent and<br>Let’s All Finish Strong!!</p>
        <svg class="signature" viewBox="0 0 110 22" role="img" aria-label="Handwritten signature of Hal Reeve">
          <rect x="0" y="4" width="110" height="14" fill="#2a3a78" opacity=".18"/>
          <line x1="4" y1="19" x2="106" y2="19" stroke="var(--ink)" stroke-width="1"/>
        </svg>
        <p class="credit">Harlan (Hal) Reeve, CPA, CFP<br>Founder and President<br>Harlan Reeve Wealth Group</p>
      </div>
    </div>
    <div class="postage">Postage<br>Area</div>
  </section>

</div>
</body>
</html>
```